Surviving Domestic Violence Flyer

I need a flyer that "POPS" to attract participants for my research project. I have added the important information on my draft flyer.

```html
<!DOCTYPE html>
<html lang="en">
<head>
<meta charset="utf-8">
<title>Survivor Research Study Flyer</title>
<link rel="stylesheet" href="https://fonts.googleapis.com/css2?family=Anton&family=Montserrat:wght@300;400;600;700&display=swap">
<style>
  :root {
    --page-bg: #ececec;
    --dark: #2d2622;
    --photo-light: #cfc9bd;
    --photo-mid: #8a8275;
    --photo-dark: #2b2824;
    --title-pill: rgba(240, 90, 215, 0.88);
    --magenta: #ff1aff;
    --question-box: rgba(160, 30, 160, 0.82);
    --bullet: #ff3df0;
    --white: #ffffff;
    --body-text: #e2dedb;
    --tab-line: #8d8580;
  }
  * { margin: 0; padding: 0; box-sizing: border-box; }
  html, body {
    width: 864px;
    height: 1200px;
    overflow: hidden;
    background: var(--page-bg);
  }
  .flyer {
    position: absolute;
    left: 0;
    top: 39px;
    width: 864px;
    height: 1122px;
    background: var(--dark);
    overflow: hidden;
    font-family: "Montserrat", sans-serif;
  }
  .hero-photo {
    position: absolute;
    left: 0;
    top: 0;
    width: 864px;
    height: 573px;
    background:
      radial-gradient(ellipse 40% 55% at 58% 45%, rgba(170,140,120,0.55), transparent 70%),
      linear-gradient(180deg, var(--photo-light) 0%, var(--photo-mid) 55%, var(--photo-dark) 100%);
  }
  .title-pill {
    position: absolute;
    left: 37px;
    top: 30px;
    width: 791px;
    height: 79px;
    border-radius: 30px;
    background: var(--title-pill);
    display: flex;
    align-items: center;
    justify-content: center;
  }
  .title-pill h1 {
    font-family: "Anton", sans-serif;
    font-weight: 400;
    font-size: 56px;
    color: var(--white);
    letter-spacing: 0.5px;
    line-height: 1;
  }
  .study-title {
    position: absolute;
    left: 53px;
    top: 162px;
    font-family: "Anton", sans-serif;
    font-weight: 400;
    font-size: 50px;
    line-height: 62px;
    color: var(--magenta);
  }
  .eligibility-box {
    position: absolute;
    left: 50px;
    top: 379px;
    width: 755px;
    height: 276px;
    border-radius: 30px;
    background: var(--question-box);
    padding: 10px 24px 0 24px;
    list-style: none;
  }
  .eligibility-box li {
    position: relative;
    padding-left: 18px;
    color: var(--white);
    font-weight: 600;
    font-size: 19.5px;
    line-height: 45px;
  }
  .eligibility-box li::before {
    content: "";
    position: absolute;
    left: 0;
    top: 19px;
    width: 7px;
    height: 7px;
    border-radius: 50%;
    background: var(--bullet);
  }
  .study-details {
    position: absolute;
    left: 60px;
    top: 684px;
    width: 760px;
    color: var(--body-text);
    font-size: 14px;
    font-weight: 300;
    line-height: 18px;
  }
  .study-details p { margin-bottom: 8px; }
  .study-details strong { font-weight: 600; color: var(--white); }
  .study-details .credit { margin-bottom: 0; }
  .study-details .credit + .contact-address { margin-top: 8px; }
  .accent-band {
    position: absolute;
    left: 0;
    top: 907px;
    width: 864px;
    height: 15px;
    background: var(--magenta);
  }
  .tear-tabs {
    position: absolute;
    left: 0;
    top: 922px;
    width: 864px;
    height: 200px;
    display: flex;
  }
  .tear-tab {
    flex: 1;
    border-right: 1px dotted var(--tab-line);
    display: flex;
    align-items: center;
    justify-content: center;
    padding-top: 12px;
  }
  .tear-tab:last-child { border-right: none; }
  .tear-tab span {
    writing-mode: vertical-rl;
    transform: rotate(180deg);
    color: var(--white);
    font-size: 14px;
    line-height: 17px;
    text-align: left;
    height: 180px;
    white-space: nowrap;
  }
  .tear-tab b { font-weight: 700; }
</style>
</head>
<body>
  <main class="flyer">
    <div class="hero-photo" role="img" aria-label="Photograph of a young woman sitting curled up against a wall, head lowered"></div>

    <header class="title-pill">
      <h1>Request for Study Participants</h1>
    </header>

    <h2 class="study-title">Efficiency of resources<br>available to survivors<br>of intimate partner abuse</h2>

    <ul class="eligibility-box">
      <li>Are you eighteen years of age or older?</li>
      <li>Have you been a victim of domestic violence?</li>
      <li>Have you sought assistance with abouse in the last 12 months?</li>
      <li>Are you still in contact with the person who abused you?</li>
      <li>Are you willing and open to discussing your experience with<br>abuse and your attempts to access services or resources?</li>
    </ul>

    <section class="study-details">
      <p>If you answered yes to all of these questions, you may be eligible to participate in a study to better understand the resources needed and services expected for survivors of domestic violence.</p>
      <p>Please contact Dana Whitfield at <strong>1(555)014-2290</strong> or via e-mail<br><strong>survivorstudy@example.org</strong> for additional information.</p>
      <p>Participants will be compensated for their time.</p>
      <p class="credit"><strong>Principal Investigator:</strong> Dana Whitfield</p>
      <p class="credit"><strong>Institutional Affiliation:</strong> Lakeshore State University, Dept. of Criminology, Law and Justice</p>
      <p class="contact-address"><strong>Contact Address:</strong> Post Office Box 100200, Springfield, IL, 62704</p>
    </section>

    <div class="accent-band"></div>

    <div class="tear-tabs">
      <div class="tear-tab"><span>Survivor Research Study<br><b>1(555)014-2290</b></span></div>
      <div class="tear-tab"><span>Survivor Research Study<br><b>1(555)014-2290</b></span></div>
      <div class="tear-tab"><span>Survivor Research Study<br><b>1(555)014-2290</b></span></div>
      <div class="tear-tab"><span>Survivor Research Study<br><b>1(555)014-2290</b></span></div>
      <div class="tear-tab"><span>Survivor Research Study<br><b>1(555)014-2290</b></span></div>
      <div class="tear-tab"><span>Survivor Research Study<br><b>1(555)014-2290</b></span></div>
      <div class="tear-tab"><span>Survivor Research Study<br><b>1(555)014-2290</b></span></div>
      <div class="tear-tab"><span>Survivor Research Study<br><b>1(555)014-2290</b></span></div>
      <div class="tear-tab"><span>Survivor Research Study<br><b>1(555)014-2290</b></span></div>
      <div class="tear-tab"><span>Survivor Research Study<br><b>1(555)014-2290</b></span></div>
      <div class="tear-tab"><span>Survivor Research Study<br><b>1(555)014-2290</b></span></div>
      <div class="tear-tab"><span>Survivor Research Study<br><b>1(555)014-2290</b></span></div>
    </div>
  </main>
</body>
</html>
```